Lanterns on the Tide

I need a book cover design for a world history book written for a target audience of high school students and progressive teachers. The book is more balanced towards a world history perspective than a Western-leaning perspective. The first 500 pages deal with the major turning points in world history - from the first hominids that roamed Africa to the end of the Cold War, and the final 100 pages cover the major challenges facing the world today. The book is 95% graphic details, hopefully-engaging stories and needed facts, but there is a bit of sarcasm, verbal irony and asides thrown in to keep the reader's eyes from glossing over. I would need a cover that would appeal to any school teacher, but something that would not scare off students or the average Joe off the street.
Updates

One added note, please leave the bottom right corner -  2" height by 3" width free of text/image for the ISBN code.

As far as a central image goes, it needs to be a dynamic (avoid something readers would readily see elsewhere in their lives) image, or nothing at all.  Also, please justify all text on the back cover to the left side (avoid centering).

Reason: A few people have voiced an interest in having the deadline extended through next weekend to allow for some alterations and also the ability to take advantage of the upcoming holidays. I will take you up on this request. Thank you all again for your submissions. i've seen some very unique takes on the story/tone of the book.

Industry/Entity Type

High School

Requirements
Must have
• I've enclosed a PDF with the text for the front and back cover.

On the back cover, I'd like the quote and the initial question to stand out. I'd like the initial question to be in lower case.

For the spine, I'd like the title font to match the title front from the front cover.

The book cover needs to measure 9.25" by 13.75" with a 1.5" spine. Allow .125 inches for the bleed.

I've attached a Word Document with all the text. The layout is just a suggestion.
Should not have
• I do not want any stock images that I'll need to pay for.

```html
<!DOCTYPE html>
<html lang="en">
<head>
<meta charset="utf-8">
<title>Lanterns on the Tide — Book Cover</title>
<link rel="stylesheet" href="https://fonts.googleapis.com/css2?family=Ultra&family=Roboto+Slab:wght@700;800&display=swap">
<style>
  :root {
    --backdrop: #e9e9e9;
    --cover-top: #c0b288;
    --cover-bottom: #d9cca2;
    --title-brown: #5e3535;
    --accent-red: #b81e2d;
    --spine-red: #c01b2d;
    --spine-text: #ffffff;
    --art-tone: #8a9a70;
    --rule: #5e3535;
  }
  * { margin: 0; padding: 0; box-sizing: border-box; }
  html, body {
    width: 1200px;
    height: 900px;
    overflow: hidden;
    background: var(--backdrop);
  }
  .book {
    position: absolute;
    left: 280px;
    top: 40px;
    height: 820px;
    display: flex;
    box-shadow: 0 18px 40px rgba(0,0,0,0.18);
  }
  .spine {
    width: 89px;
    height: 100%;
    background: var(--spine-red);
    display: flex;
    align-items: center;
    justify-content: center;
  }
  .spine-text {
    writing-mode: vertical-rl;
    display: flex;
    align-items: center;
    gap: 24px;
    color: var(--spine-text);
  }
  .spine-title {
    font-family: "Ultra", serif;
    font-size: 24px;
    letter-spacing: 1px;
    text-transform: uppercase;
    white-space: nowrap;
  }
  .spine-divider {
    width: 1px;
    height: 40px;
    background: rgba(255,255,255,0.7);
    transform: rotate(35deg);
  }
  .spine-author {
    font-family: "Roboto Slab", serif;
    font-weight: 800;
    font-size: 14px;
    letter-spacing: 1.5px;
    text-transform: uppercase;
    white-space: nowrap;
  }
  .front-cover {
    position: relative;
    width: 552px;
    height: 100%;
    background: linear-gradient(180deg, var(--cover-top) 0%, var(--cover-bottom) 100%);
  }
  .cover-title {
    position: absolute;
    left: 48px;
    top: 52px;
    width: 470px;
    font-family: "Ultra", serif;
    font-weight: 400;
    font-size: 70px;
    line-height: 1;
    color: var(--title-brown);
    text-transform: uppercase;
    letter-spacing: 1px;
  }
  .cover-art {
    position: absolute;
    left: 240px;
    top: 320px;
    width: 220px;
    height: 220px;
    border-radius: 12px;
    background: radial-gradient(ellipse at center, rgba(138,154,112,0.55) 0%, rgba(138,154,112,0.2) 60%, rgba(138,154,112,0) 100%);
  }
  .cover-subtitle {
    position: absolute;
    left: 48px;
    top: 572px;
    width: 420px;
    font-family: "Roboto Slab", serif;
    font-weight: 700;
    font-size: 25px;
    line-height: 1.25;
    color: var(--accent-red);
  }
  .author-rule {
    position: absolute;
    left: 250px;
    top: 700px;
    width: 250px;
    height: 2px;
    background: var(--rule);
  }
  .author-rule::after {
    content: "";
    position: absolute;
    left: 50%;
    top: -3px;
    width: 8px;
    height: 8px;
    margin-left: -4px;
    border-radius: 50%;
    background: var(--rule);
  }
  .cover-author {
    position: absolute;
    left: 230px;
    top: 720px;
    width: 290px;
    text-align: center;
    font-family: "Roboto Slab", serif;
    font-weight: 800;
    font-size: 26px;
    letter-spacing: 2px;
    color: var(--title-brown);
    text-transform: uppercase;
    white-space: nowrap;
  }
</style>
</head>
<body>
  <div class="book">
    <div class="spine">
      <div class="spine-text">
        <span class="spine-title">Lanterns on the Tide</span>
        <span class="spine-divider"></span>
        <span class="spine-author">Marcus Hale</span>
      </div>
    </div>
    <div class="front-cover">
      <h1 class="cover-title">Lanterns<br>on the<br>Tide</h1>
      <div class="cover-art" role="img" aria-label="Hand-drawn green spinning globe with a small speech bubble"></div>
      <p class="cover-subtitle">The tales, traditions and turning points of world history and the regional challenges of today</p>
      <div class="author-rule"></div>
      <p class="cover-author">Marcus Hale</p>
    </div>
  </div>
</body>
</html>
```